Business Card Design for a Design/Build Firm

Kestrel Forge Partners, Inc. is a firm providing construction professional project management and architectural design services to an international clientele. Contemporary. "Green" movement aware. Business card to have back design/logo. Cards will be on high gloss paper

Target Market(s)

Building Developers and Owners

Industry/Entity Type

Construction

Requirements
Nice to have
• We really would like to use the acronym "KFP" as main focal point fo card design. Company will be known as KFP.
Should not have
• No globes or abstract images of buildings.

```html
<!DOCTYPE html>
<html lang="en">
<head>
<meta charset="utf-8">
<title>KFP Business Card – Front and Back</title>
<link rel="stylesheet" href="https://fonts.googleapis.com/css2?family=Source+Sans+3:wght@400;700&display=swap">
<style>
  :root {
    --brand-green: #3b6829;
    --paper: #ffffff;
    --ink: #1a1a1a;
    --canvas: #ffffff;
    --card-edge: #d9d9d9;
  }
  * { margin: 0; padding: 0; box-sizing: border-box; }
  html, body {
    width: 1200px;
    height: 900px;
    overflow: hidden;
    background: var(--canvas);
    font-family: "Source Sans 3", "Myriad Pro", Arial, sans-serif;
  }
  .canvas {
    position: relative;
    width: 1200px;
    height: 900px;
  }
  .card {
    position: absolute;
    width: 540px;
    height: 350px;
    overflow: hidden;
  }
  .card--front {
    left: 50px;
    top: 250px;
    background: var(--brand-green);
  }
  .card--back {
    left: 615px;
    top: 300px;
    background: var(--paper);
    border: 1px solid var(--card-edge);
    box-shadow: 0 3px 10px rgba(0,0,0,0.18);
  }
  .card__graphic {
    position: absolute;
    inset: 0;
    width: 100%;
    height: 100%;
  }
  .front-wordmark {
    font-family: "Source Sans 3", Arial, sans-serif;
    font-weight: 700;
    font-size: 230px;
    fill: var(--paper);
    letter-spacing: -6px;
  }
  .back-seal {
    position: absolute;
    left: 234px;
    top: -49px;
    width: 188px;
    height: 188px;
    border-radius: 50%;
    background: var(--brand-green);
    display: flex;
    align-items: flex-end;
    justify-content: center;
    padding-bottom: 52px;
  }
  .back-seal__name {
    color: var(--paper);
    font-weight: 700;
    font-size: 56px;
    line-height: 1;
    letter-spacing: -1px;
  }
  .contact {
    position: absolute;
    left: 229px;
    top: 156px;
    color: var(--ink);
    font-size: 17px;
    line-height: 1.3;
  }
  .contact__name {
    color: var(--brand-green);
    font-size: 19px;
    font-weight: 400;
  }
  .contact__role {
    font-size: 19px;
    font-weight: 700;
  }
  .contact__phones {
    list-style: none;
    margin-top: 18px;
    padding-left: 6px;
  }
  .contact__label {
    display: inline-block;
    width: 24px;
    color: var(--brand-green);
  }
  .contact__address { margin-top: 18px; }
  .contact__web { color: var(--brand-green); }
</style>
</head>
<body>
<main class="canvas">

  <section class="card card--front" aria-label="Card front">
    <svg class="card__graphic" viewBox="0 0 540 350" xmlns="http://www.w3.org/2000/svg">
      <text class="front-wordmark" x="-10" y="330" transform="rotate(-18 200 260)">KFP</text>
      <polyline points="470,0 488,152" fill="none" stroke="#ffffff" stroke-width="2"/>
      <line x1="0" y1="300" x2="540" y2="148" stroke="#ffffff" stroke-width="2"/>
      <line x1="0" y1="330" x2="540" y2="178" stroke="#ffffff" stroke-width="2"/>
    </svg>
  </section>

  <section class="card card--back" aria-label="Card back">
    <div class="back-seal">
      <span class="back-seal__name">KFP</span>
    </div>
    <div class="contact">
      <p class="contact__name">Joe Bloggs</p>
      <p class="contact__role">Position</p>
      <ul class="contact__phones">
        <li><span class="contact__label">T.</span> 01234 567890</li>
        <li><span class="contact__label">M.</span> 01234 567890</li>
      </ul>
      <p class="contact__address">Anywhere, Anytown, zip code</p>
      <p class="contact__web">www.kfpartners-build.com</p>
    </div>
  </section>

</main>
</body>
</html>
```